Banner Ad for Easter Sale

We want an Easter graphics and design that will look professional, attractive, suit our website.

We need the graphic to show our customers that we have a massive sale going on during the Easter long weekend. The sale will be for our pavers and retaining wall blocks range of products.

The dimensions are 691 x 281 pixels, and will need to have rounded edges, just like the ones that can be seen in the centre of our homepage: www.bramblecart.com.au.

This graphic will be the first to load up in the centre rotating images on the homepage.

When clicked on, the graphic will take the customer to a page that contains the discounted products. The products included in the sale are here:
http://www.bramblecart.com.au/Easter-Sale
Note that the prices may or may not change so the prices should be ignored.
Product images may be used but don't have to be used.

We would like for it to have the following texts:
"Massive Sale on this Easter Long Weekend"
"Click here to view products"
(in smaller writing) "Pavers and Retaining wall Sample Packs Reduced to $10" and in smaller writing have our long weekend contact hours:
"Extended Customer Service hours:
8am to 9pm Daily"
"Up to 50% off!"

We are open to the texts being varied.

Target Market(s)

DIY Enthusiasts, End Customers, Landscapers

Industry/Entity Type

Product

Requirements
Must have
• Dimensions being 691 x 281 pixels, and will need to have rounded edges, just like the ones that can be seen in the centre of our homepage: www.bramblecart.com.au.

```html
<!DOCTYPE html>
<html lang="en">
<head>
<meta charset="utf-8">
<title>Easter Long Weekend Sale Banner</title>
<link rel="stylesheet" href="https://fonts.googleapis.com/css2?family=Bowlby+One+SC&family=Titan+One&family=Bree+Serif&family=Roboto+Condensed:wght@800&family=Tinos:wght@700&family=Patrick+Hand&display=swap">
<style>
  :root {
    --navy: #141a6e;
    --red: #e8102a;
    --button-red: #e0162e;
    --sky-light: #f4fbff;
    --sky-mid: #a9dcf6;
    --sky-deep: #55b3ea;
    --grass-light: #8fe04a;
    --grass-dark: #2f9a12;
    --egg-pink: #f7b3b0;
    --egg-yellow: #f6d743;
    --egg-blue: #5ec1ee;
    --egg-red: #f04a2c;
    --white: #ffffff;
    --page: #ffffff;
  }
  * { margin: 0; padding: 0; box-sizing: border-box; }
  html, body { width: 1200px; height: 488px; overflow: hidden; background: var(--page); }
  .banner {
    position: absolute; left: 5px; top: 5px; width: 1190px; height: 478px;
    border-radius: 24px; overflow: hidden; display: block; text-decoration: none;
    background:
      radial-gradient(ellipse 520px 380px at 200px 250px, var(--sky-light) 0%, rgba(244,251,255,0) 75%),
      linear-gradient(180deg, var(--sky-mid) 0%, var(--sky-deep) 60%, var(--sky-mid) 100%);
  }
  .grass {
    position: absolute; left: 0; right: 0; top: 365px; bottom: 0;
    background: linear-gradient(180deg, var(--grass-light) 0%, var(--grass-dark) 100%);
  }
  .eggs {
    position: absolute; left: 17px; top: 78px; width: 356px; height: 356px;
    border-radius: 48% 48% 40% 40%;
    background: linear-gradient(135deg, var(--egg-pink) 0%, var(--egg-yellow) 35%, var(--egg-blue) 60%, var(--egg-red) 100%);
    opacity: 0.9;
  }
  .copy {
    position: absolute; left: 350px; width: 780px; text-align: center;
    color: var(--navy); white-space: nowrap; line-height: 1;
  }
  .headline { top: 34px; font-size: 0; }
  .massive { font-family: "Bowlby One SC", "Arial Black", sans-serif; font-size: 54px; }
  .sale { font-family: "Titan One", "Arial Black", sans-serif; font-size: 72px; color: var(--red); margin: 0 16px; letter-spacing: 1px; }
  .on-this { font-family: "Bree Serif", serif; font-size: 42px; }
  .occasion { top: 120px; font-size: 0; }
  .easter { font-family: "Titan One", "Arial Black", sans-serif; font-size: 60px; color: var(--red); -webkit-text-stroke: 2px var(--navy); letter-spacing: 2px; }
  .long-weekend { font-family: "Patrick Hand", "Comic Sans MS", cursive; font-size: 54px; color: var(--white); -webkit-text-stroke: 2px var(--navy); margin-left: 18px; letter-spacing: 1px; }
  .sample-offer { top: 197px; font-family: "Roboto Condensed", sans-serif; font-weight: 800; font-size: 37px; }
  .cta {
    position: absolute; left: 494px; top: 246px; width: 436px; height: 42px;
    background: var(--button-red); color: var(--white); border: 2px solid var(--white);
    font-family: "Roboto Condensed", sans-serif; font-weight: 800; font-size: 28px;
    line-height: 38px; text-align: center; letter-spacing: 0.5px;
  }
  .service-hours { top: 301px; font-family: "Tinos", serif; font-weight: 700; font-size: 24px; line-height: 26px; }
  .service-hours .hours { display: block; font-size: 31px; line-height: 32px; }
  .discount { top: 358px; font-family: "Tinos", serif; font-weight: 700; font-size: 36px; font-variant: small-caps; letter-spacing: 1px; }
</style>
</head>
<body>
  <a class="banner" href="#">
    <div class="grass" role="img" aria-label="Green grass along the bottom edge"></div>
    <div class="eggs" role="img" aria-label="Illustration of four decorated Easter eggs in pink, yellow, blue and red"></div>
    <p class="copy headline"><span class="massive">Massive</span><span class="sale">SALE!</span><span class="on-this">on this</span></p>
    <p class="copy occasion"><span class="easter">EASTER</span><span class="long-weekend">LONG WEEKEND!</span></p>
    <p class="copy sample-offer">$10 for Pavers and Retaining Sample Packs</p>
    <span class="cta">CLICK HERE TO VIEW PRODUCTS</span>
    <p class="copy service-hours">Extended Customer Service Hours:<span class="hours">8am-9pm DAILY!</span></p>
    <p class="copy discount">Up to 50% OFF!</p>
  </a>
</body>
</html>
```